Lanterns Over Saltmere - Islamic Book about death, grave and the hereafter

We need a complete redesign of an old book cover. It is a book about death, the grave, the day of judgment, hellfire and paradise. i've attached our old bookcover. you can take new colors and change completly the design. It is up to you!

```html
<!DOCTYPE html>
<html lang="en">
<head>
<meta charset="utf-8">
<title>Lanterns Over Saltmere – Cover Concepts</title>
<link rel="stylesheet" href="https://fonts.googleapis.com/css2?family=Cormorant+Garamond:wght@400;500&family=Playfair+Display:ital,wght@0,400;1,700;1,800&family=Kaushan+Script&family=Oswald:wght@500;600&family=Cinzel:wght@400;700&family=Montserrat:wght@300;400;500;600;700&family=Open+Sans:wght@400&display=swap">
<style>
:root{
  --page:#ffffff;
  --board:#eef1f4;
  --label:#6b7178;
  --white:#ffffff;
  --ink-navy:#1b2b4a;
  --teal-deep:#1e3a4a;
  --teal-mid:#4d7384;
  --mist:#f4f5f7;
  --indigo:#1c1440;
  --gold:#d9a53c;
  --pattern-teal:#2d4a50;
  --parchment:#efcf9f;
  --parchment-ink:#3b4f52;
  --night:#0d0f14;
  --storm:#3e4a5e;
  --fog-light:#c9cabf;
  --fog-dark:#3c3d37;
  --fog-ink:#3a3b36;
  --sea-band:#5b7d86;
  --sea-top:#1f3f4f;
}
*{margin:0;padding:0;box-sizing:border-box}
html,body{width:1200px;height:848px;overflow:hidden;background:var(--page)}
.sheet{position:relative;width:1200px;height:848px}
.board{position:absolute;background:var(--board)}
.board--top{left:16px;top:43px;width:1175px;height:376px}
.board--bottom{left:13px;top:426px;width:1176px;height:377px}
.cover{position:absolute;width:213px;height:340px;overflow:hidden;color:var(--white)}
.row-1{top:48px}
.row-2{top:432px}
.number{position:absolute;width:213px;text-align:center;font:400 11px/1 "Open Sans",sans-serif;color:var(--label)}
.fill{position:absolute;left:0;right:0}
.line{position:absolute;left:0;right:0;text-align:center;line-height:1;white-space:nowrap}
.caps{font-family:"Montserrat",sans-serif;text-transform:uppercase}
.author{font-size:6px;letter-spacing:3px}
.sub{font-size:4.6px;letter-spacing:1px;font-weight:500}

/* 1 & 2 moon sky */
.cover--moon{background:var(--mist)}
.cover--moon .sky{top:0;height:240px;background:radial-gradient(circle at 50% 24% ,#dfe7ea 0 9%,rgba(223,231,234,0) 15%),linear-gradient(180deg,#27495a 0%,#3f6576 38%,#6f8e9b 62%,var(--mist) 100%)}
.cover--moon .art{bottom:0;height:120px;background:linear-gradient(180deg,rgba(244,245,247,0),#d7deea)}
.cover--moon .serif{font-family:"Cormorant Garamond",serif;color:var(--white)}
.cover--moon .kicker{top:113px;font-size:9px}
.cover--moon .title{top:128px;font-size:25px;letter-spacing:.5px}
.cover--moon .sub{top:172px;font-family:"Cormorant Garamond",serif;font-size:6.6px;letter-spacing:.2px;text-transform:uppercase}
.cover--moon .author{top:22px;font-size:4.4px;letter-spacing:2.4px;font-weight:600}

/* 3 golden night */
.cover--gold{background:var(--indigo)}
.cover--gold .stars{top:0;height:110px;background:radial-gradient(circle at 50% 50%,rgba(217,165,60,.75) 0 12%,rgba(217,165,60,.15) 30%,rgba(28,20,64,0) 60%)}
.cover--gold .trees{top:218px;height:74px;background:linear-gradient(90deg,rgba(217,165,60,.55) 0 22%,rgba(28,20,64,0) 30% 70%,rgba(217,165,60,.5) 78%,rgba(90,50,30,.6) 100%)}
.cover--gold .script{font-family:"Kaushan Script",cursive}
.cover--gold .t1{top:118px;font-size:29px}
.cover--gold .t2{top:148px;font-size:14px}
.cover--gold .t3{top:164px;font-size:33px}
.cover--gold .sub{top:215px;font-weight:700;font-size:4.6px}
.cover--gold .author{top:301px;font-size:5.4px;letter-spacing:3.4px}

/* 4 lighthouse */
.cover--storm .photo{top:0;bottom:0;background:linear-gradient(180deg,#56606f 0%,#8f9aab 30%,#55606f 55%,#2a3140 78%,#1e2430 100%)}
.cover--storm .cond{font-family:"Oswald",sans-serif;font-weight:600}
.cover--storm .small{font-size:15px;letter-spacing:5px}
.cover--storm .big{font-size:33px;letter-spacing:5px}
.cover--storm .s1{top:77px}
.cover--storm .s2{top:112px}
.cover--storm .s3{top:157px}
.cover--storm .s4{top:185px}
.cover--storm .sub{top:258px;font-weight:700;font-size:5.4px;letter-spacing:1.4px}
.cover--storm .author{top:301px;font-size:5.4px;letter-spacing:3.4px}

/* 5 label on pattern */
.cover--label .pattern{top:0;bottom:0;background:var(--pattern-teal)}
.cover--label .plate{position:absolute;left:25px;top:71px;width:161px;height:93px;background:var(--parchment);border:1.5px solid #f6dfbc;outline:1px solid #b8925e;outline-offset:-5px;color:var(--parchment-ink);font-family:"Cinzel",serif}
.cover--label .plate .line{font-size:12px;letter-spacing:1.4px}
.cover--label .p1{top:17px}
.cover--label .p2{top:34px}
.cover--label .rule{position:absolute;left:58px;width:45px;top:58px;height:1px;background:var(--parchment-ink)}
.cover--label .pa{top:67px;font-size:6px!important;font-weight:700;letter-spacing:1px!important}

/* 6 milky way */
.cover--dust .photo{top:0;bottom:0;background:radial-gradient(ellipse at 45% 55%,#6a6a6a 0%,#333 45%,#0c0c0c 80%),var(--night)}
.cover--dust .ground{bottom:0;height:105px;background:linear-gradient(180deg,rgba(10,10,10,0),#080808 30%)}
.cover--dust .sub{top:29px;font-size:5.2px}
.cover--dust .script{font-family:"Kaushan Script",cursive}
.cover--dust .t1{top:70px;font-size:27px}
.cover--dust .t2{top:102px;font-size:27px}
.cover--dust .t3{top:134px;font-size:27px}
.cover--dust .quote{top:219px;font:italic 400 6px/1 "Montserrat",sans-serif;letter-spacing:.4px;color:#d8d8d8}
.cover--dust .author{top:301px;font-size:5.6px;letter-spacing:3.4px}

/* 7 star trails */
.cover--trails{background:#10141d}
.cover--trails .band{top:0;height:25px;background:#15203a}
.cover--trails .photo{top:25px;height:250px;background:radial-gradient(ellipse at 70% 75%,#3a5479 0%,#22324e 40%,#131b2b 80%)}
.cover--trails .sub{top:11px;text-align:left;left:13px;font-size:4.4px}
.cover--trails .wide{font-family:"Montserrat",sans-serif;font-weight:600;font-size:19px;letter-spacing:8px;text-align:left;left:13px}
.cover--trails .w1{top:40px}
.cover--trails .w2{top:70px}
.cover--trails .w3{top:100px;font-size:13px;letter-spacing:7px}
.cover--trails .w4{top:120px}
.cover--trails .author{top:297px;left:auto;right:9px;text-align:right;font-size:7px;letter-spacing:1.2px}

/* 8 framed galaxy */
.cover--frame{background:var(--night)}
.cover--frame .photo{left:12px;right:12px;top:13px;height:314px;background:linear-gradient(180deg,#141a2c 0%,#2a2a4a 40%,#5a3e4c 70%,#3d2a22 88%,#0f0f12 100%)}
.cover--frame .serif{font-family:"Playfair Display",serif}
.cover--frame .sub{top:24px;font-family:"Playfair Display",serif;font-size:7.2px;letter-spacing:.8px;font-weight:400}
.cover--frame .rule{position:absolute;left:38px;right:38px;height:1px;background:var(--white)}
.cover--frame .r1{top:66px}
.cover--frame .r2{top:101px}
.cover--frame .k{top:78px;font-size:11.5px;letter-spacing:1.6px}
.cover--frame .big{top:118px;font-size:33px}
.cover--frame .author{top:310px;font-size:7px;letter-spacing:1.4px}

/* 9 fog */
.cover--fog .photo{top:0;bottom:0;background:linear-gradient(180deg,#a8a89e 0%,var(--fog-light) 30%,#a9aa9f 60%,#5c5d55 85%,var(--fog-dark) 100%)}
.cover--fog .ink{color:var(--fog-ink)}
.cover--fog .sub{top:29px;font-size:5px}
.cover--fog .m{font-family:"Montserrat",sans-serif}
.cover--fog .f1{top:58px;font-size:10px;font-weight:700;letter-spacing:2.6px}
.cover--fog .f2{top:77px;font-size:22px;font-weight:300;letter-spacing:2.6px}
.cover--fog .f3{top:109px;font-size:10px;font-weight:700;letter-spacing:2.6px}
.cover--fog .f4{top:128px;font-size:22px;font-weight:300;letter-spacing:2.6px}
.cover--fog .author{top:310px;font-size:7px;letter-spacing:1.4px}

/* 10 blue forest night */
.cover--forest{background:#1a2028}
.cover--forest .photo{top:0;height:307px;background:linear-gradient(180deg,var(--sea-top) 0%,#2f5a6b 55%,#3f6f7c 70%,#1b222b 82%,#181d24 100%)}
.cover--forest .band{top:307px;bottom:0;background:var(--sea-band)}
.cover--forest .sub{top:29px;font-size:5px}
.cover--forest .pf{font-family:"Playfair Display",serif;font-style:italic;font-weight:800}
.cover--forest .t1{top:126px;font-size:23px}
.cover--forest .t2{top:160px;font-size:26px}
.cover--forest .quote{font:italic 400 7.4px/1.35 "Playfair Display",serif}
.cover--forest .q1{top:207px}
.cover--forest .q2{top:217px}
.cover--forest .author{top:320px;font-size:6.4px;letter-spacing:1.4px}
</style>
</head>
<body>
<main class="sheet">
  <div class="board board--top"></div>
  <div class="board board--bottom"></div>

  <!-- Row 1 -->
  <section class="cover cover--moon row-1" style="left:21px">
    <div class="fill sky" role="img" aria-label="Night sky photo with full moon behind clouds fading to white"></div>
    <div class="fill art" role="img" aria-label="Blue line-drawn lotus mandala illustration"></div>
    <p class="line caps author">Mira Halden-Soor</p>
    <p class="line serif kicker">LANTERNS OVER</p>
    <h1 class="line serif title">SALTMERE</h1>
    <p class="line sub">Über den Tod und das Leben danach</p>
  </section>
  <div class="number" style="left:21px;top:400px">1</div>

  <section class="cover cover--moon row-1" style="left:258px">
    <div class="fill sky" role="img" aria-label="Night sky photo with full moon behind clouds fading to white"></div>
    <div class="fill art" role="img" aria-label="Blue line-drawn city skyline illustration with domes and minarets"></div>
    <p class="line caps author">Mira Halden-Soor</p>
    <p class="line serif kicker">LANTERNS OVER</p>
    <h1 class="line serif title">SALTMERE</h1>
    <p class="line sub">Über den Tod und das Leben danach</p>
  </section>
  <div class="number" style="left:258px;top:400px">2</div>

  <section class="cover cover--gold row-1" style="left:495px">
    <div class="fill stars" role="img" aria-label="Gold star burst surrounded by scattered gold stars"></div>
    <div class="fill trees" role="img" aria-label="Gold textured tree illustrations at the lower corners"></div>
    <p class="line script t1">Lanterns</p>
    <p class="line script t2">Over</p>
    <h1 class="line script t3">Saltmere</h1>
    <p class="line caps sub">Über den Tod und das Leben danach</p>
    <p class="line caps author">Mira Halden-Soor</p>
  </section>
  <div class="number" style="left:495px;top:400px">3</div>

  <section class="cover cover--storm row-1" style="left:731px">
    <div class="fill photo" role="img" aria-label="Stormy sea photo with waves crashing against a lighthouse"></div>
    <p class="line cond small s1">LANTERNS</p>
    <p class="line cond big s2" style="font-size:22px;letter-spacing:3px">LANTERNS</p>
    <p class="line cond small s3">OVER</p>
    <h1 class="line cond big s4">SALTMERE</h1>
    <p class="line caps sub">Über den Tod und das Leben danach</p>
    <p class="line caps author">Mira Halden-Soor</p>
  </section>
  <div class="number" style="left:731px;top:400px">4</div>

  <section class="cover cover--label row-1" style="left:968px">
    <div class="fill pattern" role="img" aria-label="Dark teal background with copper and cream floral pattern"></div>
    <div class="plate">
      <p class="line p1">LANTERNS OVER</p>
      <h1 class="line p2">SALTMERE</h1>
      <div class="rule"></div>
      <p class="line pa">MIRA HALDEN-SOOR</p>
    </div>
  </section>
  <div class="number" style="left:968px;top:400px">5</div>

  <!-- Row 2 -->
  <section class="cover cover--dust row-2" style="left:19px">
    <div class="fill photo" role="img" aria-label="Milky way night sky photo"></div>
    <div class="fill ground" role="img" aria-label="Silhouette of a person standing on a dark hill"></div>
    <p class="line caps sub">Über den Tod und das Leben danach</p>
    <p class="line script t1">Lanterns</p>
    <p class="line script t2">Over</p>
    <h1 class="line script t3">Saltmere</h1>
    <p class="line quote">“Amazing... A must-read.” —Tide Readers</p>
    <p class="line caps author">Mira Halden-Soor</p>
  </section>
  <div class="number" style="left:19px;top:784px">6</div>

  <section class="cover cover--trails row-2" style="left:257px">
    <div class="fill band"></div>
    <div class="fill photo" role="img" aria-label="Swirling star trails photo over a seated silhouette"></div>
    <p class="line caps sub">Über den Tod und das Leben danach</p>
    <p class="line wide w1">LANTERNS</p>
    <p class="line wide w2">OVER</p>
    <h1 class="line wide w4" style="top:100px">SALTMERE</h1>
    <p class="line caps author">Mira Halden-Soor</p>
  </section>
  <div class="number" style="left:257px;top:784px">7</div>

  <section class="cover cover--frame row-2" style="left:493px">
    <div class="fill photo" role="img" aria-label="Purple galaxy sky photo with a lone figure standing on a rock"></div>
    <p class="line sub">ÜBER DEN TOD UND DAS LEBEN DANACH</p>
    <div class="rule r1"></div>
    <p class="line serif k">LANTERNS OVER</p>
    <div class="rule r2"></div>
    <h1 class="line serif big">SALTMERE</h1>
    <p class="line caps author">Mira Halden-Soor</p>
  </section>
  <div class="number" style="left:493px;top:784px">8</div>

  <section class="cover cover--fog row-2" style="left:730px">
    <div class="fill photo" role="img" aria-label="Foggy forest photo with a figure walking away"></div>
    <p class="line caps sub ink">Über den Tod und das Leben danach</p>
    <p class="line m ink f1">LANTERNS</p>
    <p class="line m ink f2" style="top:74px">LANTERNS</p>
    <p class="line m ink f3">OVER</p>
    <h1 class="line m ink f4">SALTMERE</h1>
    <p class="line caps author">Mira Halden-Soor</p>
  </section>
  <div class="number" style="left:730px;top:784px">9</div>

  <section class="cover cover--forest row-2" style="left:967px">
    <div class="fill photo" role="img" aria-label="Starry blue night sky over a dark pine forest"></div>
    <div class="fill band"></div>
    <p class="line caps sub">Über den Tod und das Leben danach</p>
    <p class="line pf t1">Lanterns Over</p>
    <h1 class="line pf t2">Saltmere</h1>
    <p class="line quote q1">“They were perfectly aligned –</p>
    <p class="line quote q2">then the earth went dark.”</p>
    <p class="line caps author">Mira Halden-Soor</p>
  </section>
  <div class="number" style="left:967px;top:784px">10</div>
</main>
</body>
</html>
```